Boutique furnished offices with "high end" childcare centre require Wordpress website template

Project Overview: We require a wordpress design for a new company based in Kestrel Point Western Australia, "The Harbour 19 Collective" which provide centres where parents can utilise childcare whilst hiring furnished offices and co-working spaces. We also provide onsite beauty, hair, gymnasium and park & ride facilities into the CBD which can all be booked online through our website (plugins required to be used to book through https://quickslotter.example/). We are a one stop shop where you can drop your children at childcare, skip the traffic and ride the ferry into the CBD. Or simply have your children cared for whilst you work out of our furnished office facilities.
The website design should be classy, modern, gender neutral and corporate (not too children focused/playful).

Look And Feel: clean, classy, modern site which is easy to navigate and book services online. It must also be gender neutral and corporate (not children focused/playful).
A typical childcare centre feel - we aren’t going for "jellybeans and teddybears" we are looking for a classy, corporate and sophisticated feel.

(LOGO currently being finalised but is charcoal grey on a white back ground and attached below - but will all be in lower case not capitals)

Target Market(s)

Target market is working parents, predominantly corporate or consultants running their own businesses.

Industry/Entity Type

Boutique

Number of Pages Required

2 page

Requirements
Must have
• The following would be required of the winning submission:
• • Clean, classy, modern site which is easy to navigate and book services online. It must also be gender neutral and corporate (not children focused/playful).
• • Require simplistic homepage with Menu of list of services, and template for individual pages for each of the services offered (child care, furnished offices, park & ride, hair/ beauty, gymnasium)
• • Necessary customization/plugins to allow online bookings to be placed https://quickslotter.example/
• • Well placed plugin/customization to link and also allow "share it" type links to major social networks (linkedin, facebook, twitter, google+, etc.).
• • All design components should be optimized for indexing on major search engines
• • Wordpress theme that is supported in Chrome, IE 8+, firefox, and safari
Nice to have
• Included below is a list of sites that we like from a simplicity and clean look and feel.
• http://www.lumenfold.example.au/
• http://www.wanderthegardenpath.example.uk/
• http://www.velopiccolo.example/
• http://www.qvframe.example.au/
• http://madebymarten.example/

```html
<!DOCTYPE html>
<html lang="en">
<head>
<meta charset="utf-8">
<title>The Harbour 19 Collective</title>
<link href="https://fonts.googleapis.com/css2?family=Roboto:wght@400;500;700&family=Open+Sans:wght@400;600;700&display=swap" rel="stylesheet">
<style>
:root{
  --orange:#f5863b;
  --orange-soft:#f9b98a;
  --cream:#fdf6e8;
  --paper:#ffffff;
  --mist:#f6f6f8;
  --ink:#4d4d4d;
  --title:#5a5a5a;
  --muted:#8a8a8a;
  --line:#dcdcdc;
  --blue:#3d7fd9;
  --purple:#8a6fd6;
  --pink:#e8708a;
  --footer:#6b6b6b;
  --footer-dark:#4a4a4a;
}
*{box-sizing:border-box;margin:0;padding:0}
html,body{width:1200px;height:4054px;overflow:hidden}
body{position:relative;font-family:"Open Sans",Arial,sans-serif;color:var(--ink);background:var(--paper)}
.abs{position:absolute}
a{color:inherit;text-decoration:none}

/* header */
.site-header{position:absolute;left:0;top:0;width:1200px;height:95px;background:var(--cream)}
.main-nav a{position:absolute;top:50px;font:600 13px "Open Sans",sans-serif;color:#555;letter-spacing:.3px;white-space:nowrap}
.header-social{position:absolute;top:8px;left:872px;display:flex;gap:6px}
.header-social span{width:22px;height:22px;border:1px solid #9a9a9a;border-radius:50%}
.brand{position:absolute;left:490px;top:36px;width:220px;height:40px;display:flex;align-items:center;justify-content:center;gap:8px;font:500 19px "Roboto",sans-serif;color:#4a4a4a;letter-spacing:.5px;white-space:nowrap}
.brand i{width:14px;height:14px;border-radius:50%;background:#4a4a4a;display:block}
.search-btn{position:absolute;left:989px;top:40px;width:38px;height:38px;background:var(--orange)}
.dropdown{position:absolute;left:319px;top:100px;width:197px;background:#fff;box-shadow:0 3px 8px rgba(0,0,0,.2);z-index:5}
.dropdown a{display:block;height:31px;line-height:31px;padding-left:16px;font:600 11px "Open Sans",sans-serif;color:#555;border-bottom:1px solid #eee}
.dropdown a:last-child{border-bottom:3px solid var(--orange)}

/* hero */
.hero{position:absolute;left:0;top:95px;width:1200px;height:481px}
.hero-photo{position:absolute;top:0;height:481px}
.hero-caption{position:absolute;left:387px;top:170px;width:424px;height:155px;background:rgba(0,0,0,.75);text-align:center;color:#fff}
.hero-caption p{font:500 18px "Roboto",sans-serif;letter-spacing:.5px;margin-top:22px;line-height:26px}
.btn{display:inline-block;background:var(--orange);color:#fff;font:600 14px "Open Sans",sans-serif;border-radius:3px;text-align:center;white-space:nowrap}
.hero-caption .btn{margin-top:20px;width:114px;height:37px;line-height:37px}
.slide-arrow{position:absolute;top:311px;width:35px;height:49px;background:rgba(0,0,0,.75)}

/* badges */
.badge{position:absolute;left:570px;width:60px;height:60px;border-radius:50%;z-index:3}
.badge.solid{background:var(--orange);border:5px solid #fff;box-shadow:0 0 0 1px var(--line)}
.badge.ring{background:var(--paper);border:1px solid var(--line)}

/* sections */
.section-title{position:absolute;left:0;width:1200px;text-align:center;font:700 42px "Roboto",sans-serif;color:var(--title);letter-spacing:1px}
.title-rule{position:absolute;left:555px;width:90px;height:2px;background:var(--orange)}
.about{position:absolute;left:0;top:576px;width:1200px;height:438px;background:var(--cream)}
.about-text{position:absolute;left:275px;top:140px;width:650px;text-align:center;font:400 16px/25px "Open Sans",sans-serif;color:#8a8a8a}
.about .btn{position:absolute;left:541px;top:342px;width:118px;height:36px;line-height:36px;border-radius:18px;font-size:12px;background:var(--orange-soft)}

.services{position:absolute;left:0;top:1014px;width:1200px;height:1089px;background:var(--mist);border-top:1px solid var(--line)}
.card{position:absolute;background:#fff;box-shadow:0 3px 8px rgba(0,0,0,.12)}
.card-title{position:absolute;left:0;top:0;font:400 18px "Roboto",sans-serif;padding-left:16px;border-left:4px solid;white-space:nowrap}
.card-text{position:absolute;font:400 13px/19px "Open Sans",sans-serif;color:#888}
.card-text.small{font-size:12px;line-height:17px}
.more{position:absolute;font:600 12px "Open Sans",sans-serif;color:#444;white-space:nowrap}
.ph{position:absolute}

.experts{position:absolute;left:0;top:2103px;width:1200px;height:559px;background:var(--cream);border-top:1px solid var(--line)}
.expert{position:absolute;top:200px;width:260px;text-align:center}
.expert .avatar{width:124px;height:124px;border-radius:50%;border:4px solid #fff;box-shadow:0 0 0 2px var(--orange-soft);margin:0 auto}
.expert h3{font:700 17px "Open Sans",sans-serif;color:#333;margin-top:25px}
.expert p{font:400 13px/18px "Open Sans",sans-serif;color:#999;margin-top:10px}
.dots{display:flex;justify-content:center;gap:6px;margin-top:16px}
.dots span{width:30px;height:30px;border-radius:50%}
.car-arrow{position:absolute;top:2420px;width:30px;height:32px;background:#666}

.news{position:absolute;left:0;top:2662px;width:1200px;height:657px;background:#fff;border-top:1px solid var(--line)}
.news-card{position:absolute;top:198px;width:268px;height:346px;background:#fff;box-shadow:0 2px 8px rgba(0,0,0,.12)}
.news-card h4{position:absolute;left:14px;top:178px;width:240px;font:400 16px/21px "Open Sans",sans-serif}
.news-card p{position:absolute;left:14px;top:230px;width:240px;font:400 12px/17px "Open Sans",sans-serif;color:#aaa}
.news-bar{position:absolute;left:0;bottom:0;width:268px;height:36px;color:#fff;font:600 12px/36px "Open Sans",sans-serif;padding-left:18px}
.news-bar i{position:absolute;top:12px;width:14px;height:12px;border:2px solid #fff;border-radius:2px}
.view-all{position:absolute;left:543px;top:595px;width:114px;height:34px;border:2px solid #555;border-radius:17px;text-align:center;font:600 13px/30px "Open Sans",sans-serif;color:#444}

.map{position:absolute;left:0;top:3319px;width:1200px;height:346px;background:linear-gradient(135deg,#e4e4e4,#d6d6d6)}

.site-footer{position:absolute;left:0;top:3665px;width:1200px;height:341px;background:var(--footer);color:#fff}
.site-footer h5{position:absolute;top:34px;font:700 20px "Roboto",sans-serif}
.site-footer .rule{position:absolute;top:66px;width:110px;height:1px;background:#9a9a9a}
.contact-line{position:absolute;left:173px;font:400 13px "Open Sans",sans-serif;white-space:nowrap}
.contact-line svg{position:absolute;left:0;top:2px}
.contact-line span{margin-left:36px}
.field{position:absolute;background:#e6e6e6;color:#999;font:400 13px "Open Sans",sans-serif;padding:8px 10px;border-radius:2px}
.foot-social{position:absolute;left:205px;top:225px;display:flex;gap:8px}
.foot-social span{width:32px;height:32px;border-radius:50%;background:#4a97d4}
.footer-bar{position:absolute;left:0;top:4006px;width:1200px;height:48px;background:var(--footer-dark);color:#fff;font:400 11px/48px "Open Sans",sans-serif}
.footer-bar span{white-space:nowrap}
</style>
</head>
<body>

<header class="site-header">
  <div class="header-social"><span></span><span></span><span></span><span></span></div>
  <nav class="main-nav">
    <a href="#" style="left:210px">HOME</a>
    <a href="#" style="left:266px">OUR STORY</a>
    <a href="#" style="left:353px">OUR SERVICES ▾</a>
    <a href="#" style="left:747px">PARENTS</a>
    <a href="#" style="left:821px">NEWS</a>
    <a href="#" style="left:876px">CONTACT US</a>
  </nav>
  <div class="brand"><i></i>harbour 19 collective</div>
  <div class="search-btn">
    <svg width="38" height="38" viewBox="0 0 38 38"><circle cx="17" cy="17" r="7" fill="none" stroke="#fff" stroke-width="2.5"/><line x1="22" y1="22" x2="28" y2="28" stroke="#fff" stroke-width="2.5"/></svg>
  </div>
</header>

<section class="hero">
  <div class="hero-photo" role="img" aria-label="Bright childcare playroom with toys and play mats" style="left:0;width:600px;background:linear-gradient(160deg,#6a8ccf 0%,#c9b27c 45%,#8a5a3a 100%)"></div>
  <div class="hero-photo" role="img" aria-label="Glass-walled furnished meeting office" style="left:600px;width:600px;background:linear-gradient(160deg,#d9dde2 0%,#9aa0a6 45%,#5a4636 100%)"></div>
  <div class="hero-caption">
    <p>THE BEST OF CHILDCARE WITH FURNISHED<br>OFFICE FOR PARENTS</p>
    <a class="btn" href="#">Book Now</a>
  </div>
  <div class="slide-arrow" style="left:92px"><svg width="35" height="49"><polyline points="21,16 13,24.5 21,33" fill="none" stroke="#fff" stroke-width="2"/></svg></div>
  <div class="slide-arrow" style="left:1108px"><svg width="35" height="49"><polyline points="14,16 22,24.5 14,33" fill="none" stroke="#fff" stroke-width="2"/></svg></div>
</section>

<nav class="dropdown">
  <a href="#">CHILDCARE</a><a href="#">FURNISHED OFFICES</a><a href="#">PARK &amp; RIDE</a><a href="#">HAIR / BEAUTY</a><a href="#">GYMNASIUM</a>
</nav>

<section class="about">
  <h2 class="section-title" style="top:52px">ABOUT US</h2>
  <div class="title-rule" style="top:110px"></div>
  <p class="about-text">Nam libero tempore cum soluta nobis est eligendi optio cumque nihil impedit quo minus id quod maxime placeat facere possimus, omnis voluptas assumenda est omnis dolor repellendus. Temporibus autem quibusdam et aut officiis debitis aut rerum necessitatibus saepe eveniet ut et voluptates repudiandae sint et molestiae non recusandae.Itaque earum rerum hic tenetur a sapiente delectus, ut aut reiciendis voluptatibus maiores alias consequatur aut perferendis doloribus asperiores</p>
  <a class="btn" href="#">Read More</a>
</section>
<div class="badge solid" style="top:546px"><svg width="50" height="50"><rect x="17" y="15" width="16" height="20" rx="2" fill="none" stroke="#fff" stroke-width="2"/><line x1="21" y1="22" x2="29" y2="22" stroke="#fff" stroke-width="2"/><line x1="21" y1="27" x2="29" y2="27" stroke="#fff" stroke-width="2"/></svg></div>

<section class="services">
  <h2 class="section-title" style="top:50px">OUR SERVICES</h2>
  <div class="title-rule" style="top:116px"></div>

  <article class="card" style="left:249px;top:202px;width:340px;height:400px">
    <h3 class="card-title" style="border-color:var(--blue);color:var(--blue);top:12px">Child Care</h3>
    <div class="ph" role="img" aria-label="Carer reading with young children at a table" style="left:0;top:44px;width:340px;height:213px;background:linear-gradient(135deg,#8fb0d8,#d5c0b0 60%,#5e7da8)"></div>
    <p class="card-text" style="left:12px;top:276px;width:316px">Duis aute irure dolor in reprehenderit in voluptate velit esse cillum dolore eu fugiat nulla pariatur occaecat cupidatat non proident</p>
    <a class="more" href="#" style="left:12px;top:343px">Read More</a>
  </article>

  <article class="card" style="left:611px;top:167px;width:340px;height:408px">
    <h3 class="card-title" style="border-color:var(--orange);color:var(--orange);top:12px">Furnished Offices</h3>
    <div class="ph" role="img" aria-label="Open plan furnished office with desks" style="left:0;top:49px;width:340px;height:216px;background:linear-gradient(135deg,#dadcdf,#8c9096 60%,#b23a32)"></div>
    <p class="card-text" style="left:12px;top:284px;width:316px">Et harum quidem rerum facilis est et expedita distinctio. Nam libero tempore, cum soluta nobis est eligendi optio cumque nihil impedit</p>
    <a class="more" href="#" style="left:12px;top:352px">Read More</a>
  </article>

  <article class="card" style="left:249px;top:627px;width:340px;height:400px">
    <h3 class="card-title" style="border-color:#b45ad0;color:var(--purple);top:12px">Park &amp; Ride</h3>
    <div class="ph" role="img" aria-label="Colourful caterpillar ride at a park" style="left:0;top:43px;width:340px;height:213px;background:linear-gradient(135deg,#dfe6ea,#6ea85a 50%,#8ea2b0)"></div>
    <p class="card-text" style="left:12px;top:277px;width:316px">Itaque earum rerum hic tenetur a sapiente delectus ut aut reiciendis voluptatibus maiores alias consequatur aut perferendis doloribus</p>
    <a class="more" href="#" style="left:12px;top:343px">Read More</a>
  </article>

  <article class="card" style="left:611px;top:597px;width:340px;height:189px;background:#f1f1f1">
    <div class="ph" role="img" aria-label="Portrait showing long styled hair" style="left:0;top:0;width:146px;height:189px;background:linear-gradient(135deg,#2a2a2a,#8a8a8a 55%,#1c1c1c)"></div>
    <h3 class="card-title" style="left:160px;top:30px;border:0;padding:0;color:var(--pink)">Hair / Beauty</h3>
    <p class="card-text small" style="left:160px;top:60px;width:172px">Temporibus autem quibusdam et aut officiis debitis aut rerum necessitatibus saepe</p>
    <a class="more" href="#" style="left:160px;top:140px;color:#555">Read More</a>
  </article>

  <article class="card" style="left:611px;top:811px;width:340px;height:191px">
    <div class="ph" role="img" aria-label="Gym machine workout in black and white" style="left:0;top:0;width:146px;height:191px;background:linear-gradient(135deg,#dcdcdc,#6a6a6a 60%,#bdbdbd)"></div>
    <h3 class="card-title" style="left:160px;top:30px;border:0;padding:0;color:var(--blue)">Gymnasium</h3>
    <p class="card-text small" style="left:160px;top:60px;width:172px">Omnis iste natus error sit totam rem aperiam eaque ipsa quae ab illo inventore veritatis</p>
    <a class="more" href="#" style="left:160px;top:140px;color:var(--pink)">Read More</a>
  </article>
</section>
<div class="badge ring" style="top:981px"><svg width="58" height="58"><rect x="19" y="19" width="20" height="20" fill="none" stroke="var(--orange)" stroke-width="2"/><line x1="29" y1="19" x2="29" y2="39" stroke="var(--orange)" stroke-width="2"/><line x1="19" y1="29" x2="39" y2="29" stroke="var(--orange)" stroke-width="2"/></svg></div>

<section class="experts">
  <h2 class="section-title" style="top:68px">OUR EXPERTS</h2>
  <div class="title-rule" style="top:132px"></div>
  <div class="expert" style="left:178px">
    <div class="avatar" role="img" aria-label="Expert portrait" style="background:linear-gradient(135deg,#f2e6dc,#c9b29e)"></div>
    <h3>Owen Ridley</h3>
    <p>Duis aute irure dolor in reprehenderit in voluptate velit esse cillum dolore</p>
    <div class="dots"><span style="background:#3b6bb0"></span><span style="background:#3fa9e0"></span><span style="background:#d9534f"></span></div>
  </div>
  <div class="expert" style="left:462px">
    <div class="avatar" role="img" aria-label="Expert portrait" style="background:linear-gradient(135deg,#f3e8dc,#d2b48f)"></div>
    <h3>Clara Whitfield</h3>
    <p>Rerum necessitatibus saepe eveniet ut et voluptates repudiandae sint et</p>
    <div class="dots"><span style="background:#3b6bb0"></span><span style="background:#3fa9e0"></span><span style="background:#d9534f"></span></div>
  </div>
  <div class="expert" style="left:757px">
    <div class="avatar" role="img" aria-label="Expert portrait" style="background:linear-gradient(135deg,#eef0f2,#b8a48c)"></div>
    <h3>Mira Solberg</h3>
    <p>Excepteur sint occaecat cupidatat non proident sunt in culpa qui officia</p>
    <div class="dots"><span style="background:#3b6bb0"></span><span style="background:#3fa9e0"></span><span style="background:#d9534f"></span></div>
  </div>
</section>
<div class="car-arrow" style="left:142px"><svg width="30" height="32"><polyline points="18,10 12,16 18,22" fill="none" stroke="#fff" stroke-width="2"/></svg></div>
<div class="car-arrow" style="left:1028px"><svg width="30" height="32"><polyline points="12,10 18,16 12,22" fill="none" stroke="#fff" stroke-width="2"/></svg></div>
<div class="badge ring" style="top:2073px"><svg width="58" height="58"><circle cx="29" cy="25" r="6" fill="none" stroke="var(--orange)" stroke-width="2"/><path d="M19 39c1-7 19-7 20 0" fill="none" stroke="var(--orange)" stroke-width="2"/></svg></div>

<section class="news">
  <h2 class="section-title" style="top:62px">LATEST NEWS</h2>
  <div class="title-rule" style="top:120px"></div>

  <article class="news-card" style="left:173px">
    <div class="ph" role="img" aria-label="Children playing with a carer indoors" style="left:0;top:0;width:268px;height:162px;background:linear-gradient(135deg,#4f6fa8,#e0c9a0 55%,#b0493a)"></div>
    <h4 style="color:var(--orange)">Neque porro quisquam est dolor ipsum quia</h4>
    <p>Ullam corporis suscipit laboriosam nisi ut aliquid ex ea commodi consequatur vel eum iure</p>
    <div class="news-bar" style="background:var(--orange-soft)">Read More<i style="left:204px"></i><i style="left:236px;border-radius:50%;width:12px"></i></div>
  </article>
  <article class="news-card" style="left:465px">
    <div class="ph" role="img" aria-label="People training on treadmills" style="left:0;top:0;width:268px;height:162px;background:linear-gradient(135deg,#e8e8e8,#8e8e8e 55%,#d0d0d0)"></div>
    <h4 style="color:#aaa">Molestias excepturi sint occaecati cupiditate</h4>
    <p>Nihil impedit quo minus id quod maxime placeat facere possimus omnis voluptas assumenda est omnis</p>
    <div class="news-bar" style="background:#b3b3b3">Read More<i style="left:204px"></i><i style="left:236px;border-radius:50%;width:12px"></i></div>
  </article>
  <article class="news-card" style="left:760px">
    <div class="ph" role="img" aria-label="Families on a fairground ride" style="left:0;top:0;width:268px;height:162px;background:linear-gradient(135deg,#c8423a,#5a7ea8 55%,#e0d4c0)"></div>
    <h4 style="color:var(--purple)">Reiciendis voluptatibus maiores alias consequatur</h4>
    <p>Quis autem vel eum iure reprehenderit qui in ea voluptate velit esse quam nihil molestiae</p>
    <div class="news-bar" style="background:#a690e0">Read More<i style="left:204px"></i><i style="left:236px;border-radius:50%;width:12px"></i></div>
  </article>

  <a class="view-all" href="#">View All</a>
</section>
<div class="badge ring" style="top:2632px"><svg width="58" height="58"><rect x="17" y="20" width="24" height="18" fill="none" stroke="var(--orange)" stroke-width="2"/><line x1="21" y1="26" x2="37" y2="26" stroke="var(--orange)" stroke-width="2"/><line x1="21" y1="31" x2="37" y2="31" stroke="var(--orange)" stroke-width="2"/></svg></div>

<div class="map" role="img" aria-label="Street map showing the centre location"></div>
<svg class="abs" style="left:278px;top:3440px" width="28" height="40" viewBox="0 0 28 40"><path d="M14 0C6 0 0 6 0 14c0 10 14 26 14 26s14-16 14-26C28 6 22 0 14 0z" fill="#e8674a"/><circle cx="14" cy="14" r="5" fill="#fff"/></svg>

<footer class="site-footer">
  <h5 style="left:173px">Contact Us</h5><div class="rule" style="left:173px"></div>
  <div class="contact-line" style="top:88px"><svg width="14" height="18"><path d="M7 0C3 0 0 3 0 7c0 5 7 11 7 11s7-6 7-11c0-4-3-7-7-7z" fill="#fff"/></svg><span>Kestrel Point, Bayside District</span></div>
  <div class="contact-line" style="top:121px"><svg width="16" height="16"><path d="M3 1l3 0 1 4-2 1c1 2 3 4 5 5l1-2 4 1 0 3c0 1-1 2-2 2C7 15 1 9 1 3c0-1 1-2 2-2z" fill="#fff"/></svg><span>+61 8 5550 1919</span></div>
  <div class="contact-line" style="top:150px"><svg width="16" height="14"><rect x="0" y="1" width="16" height="12" fill="#fff"/><polyline points="0,1 8,8 16,1" fill="none" stroke="#6b6b6b" stroke-width="1.5"/></svg><span>hello@harbour19collective.example</span></div>
  <div class="contact-line" style="top:180px"><svg width="16" height="16"><circle cx="8" cy="8" r="7" fill="#fff"/><path d="M1 8h14M8 1c-3 4-3 10 0 14M8 1c3 4 3 10 0 14" fill="none" stroke="#6b6b6b"/></svg><span>harbour19collective.example</span></div>
  <div class="foot-social"><span></span><span style="background:#4ab3e8"></span><span style="background:#d9534f"></span><span style="background:#2a7fb8"></span></div>

  <h5 style="left:462px">Quick Contact</h5><div class="rule" style="left:462px"></div>
  <div class="field" style="left:462px;top:87px;width:260px;height:32px">Name...</div>
  <div class="field" style="left:462px;top:127px;width:260px;height:32px">Email...</div>
  <div class="field" style="left:462px;top:167px;width:260px;height:78px">Message...</div>
  <div class="abs btn" style="left:660px;top:258px;width:62px;height:30px;line-height:30px;font-size:11px;background:var(--orange-soft)">Submit</div>

  <h5 style="left:757px">Newsletter</h5><div class="rule" style="left:757px"></div>
  <p class="abs" style="left:765px;top:88px;width:250px;font:400 13px/19px 'Open Sans',sans-serif">Subscribe to our newsletter for latest updates</p>
  <div class="field" style="left:765px;top:140px;width:188px;height:32px">Email...</div>
  <div class="abs btn" style="left:953px;top:140px;width:74px;height:32px;line-height:32px;font-size:12px;background:var(--orange-soft);border-radius:0 2px 2px 0">Subscribe</div>
  <div class="abs btn" style="left:827px;top:215px;width:133px;height:36px;line-height:32px;background:#5b9de6;border:2px solid #bcd6f5">Book Now</div>
</footer>

<div class="footer-bar">
  <span class="abs" style="left:185px">©Copyright information here</span>
  <span class="abs" style="left:692px">Home | About Us | Services | Experts | Contact Us | Privacy Policy</span>
</div>
<div class="abs" style="left:572px;top:3978px;width:56px;height:56px;border-radius:50%;background:var(--footer-dark);border:3px solid #fff">
  <svg width="50" height="50"><circle cx="25" cy="25" r="18" fill="var(--orange)"/><path d="M25 15c-5 0-8 4-8 8 0 5 8 12 8 12s8-7 8-12c0-4-3-8-8-8z" fill="none" stroke="#fff" stroke-width="2"/></svg>
</div>

</body>
</html>
```